Media and Film Company Needs a New Website

We produce highly stylized commercials and film pieces for our clients. We also produce live events, both corporate and theatrical. Looking for a site that can show off our client videos - have a polished way to show off our team, and be able to create pages to highlight our clients and give a full overview of our project/process with them. We design simple website for some of our clients - so we are very wordpress familiar, and would like something that doesn't feel like a template.

Target Market(s)

content creators, creative directors, production teams, marketing agencies

Industry/Entity Type

Film Production

Number of Pages Required

4 page

Font styles to use
Sans Serif

Requirements
Must have
• slick looking video embed (from YT or Streamly)
• project pages - client snapshot (what we did for them, how we did it)
• nice landing page, have our company video reel on the page
• testimonials
• contact page
• ability to have photos as a background if we want
Nice to have
• polished clean look - look to our logo colors and linear elements
• we produce very stylized videos for our clients and our website should reflect that
Should not have
• template look or feel to it- please bring your flare to the project!
• take a look at our current site - zantorvo.com we need a better way to highlight our work and our clients

```html
<!DOCTYPE html>
<html lang="en">
<head>
<meta charset="utf-8">
<title>Velnaro Media &amp; Entertainment</title>
<link href="https://fonts.googleapis.com/css2?family=Lato:wght@300;400;700;900&family=Open+Sans:wght@400;600;700&display=swap" rel="stylesheet">
<style>
:root{
  --gold:#f2b824;
  --pink:#d8226b;
  --blue:#2c84c8;
  --ink:#2a2a2a;
  --muted:#666;
  --dark:#141414;
  --footer:#1f1613;
  --grey:#ececec;
  --line:#cfcfcf;
}
*{margin:0;padding:0;box-sizing:border-box}
html,body{width:1200px;height:3696px;overflow:hidden}
body{position:relative;background:#fff;font-family:"Open Sans",Arial,sans-serif;color:var(--ink)}
.abs{position:absolute}
h1,h2,h3,h4{font-family:"Lato",Arial,sans-serif;font-weight:400}

/* header */
.site-header{position:absolute;left:0;top:0;width:1200px;height:111px;background:#fff;border-bottom:1px solid #e5e5e5}
.brand{position:absolute;left:99px;top:34px;display:flex;align-items:center;gap:10px}
.brand-mark{width:30px;height:30px;background:var(--gold)}
.brand-name{font-family:"Lato",sans-serif;font-weight:700;font-size:26px;color:#333;line-height:1}
.brand-sub{font-family:"Lato",sans-serif;font-weight:700;font-size:11px;color:#333;letter-spacing:2px;position:absolute;left:140px;top:70px}
.socials-top{position:absolute;left:727px;top:6px;display:flex;gap:6px}
.socials-top span{width:22px;height:22px;border-radius:50%;background:var(--blue)}
.phone-pill{position:absolute;left:905px;top:2px;width:172px;height:30px;background:var(--blue);border-radius:0 0 14px 14px;color:#fff;font-size:15px;display:flex;align-items:center;justify-content:center;gap:8px}
.main-nav{position:absolute;left:420px;top:68px;display:flex;font-size:13px;font-family:"Open Sans",sans-serif;color:#333}
.main-nav a{padding:0 14px;border-right:1px solid #ccc;line-height:14px;text-decoration:none;color:inherit}
.main-nav a:last-child{border-right:0}
.main-nav a.active{color:var(--pink);border-right:1px solid #ccc;position:relative}
.main-nav a.active::after{content:"";position:absolute;left:14px;right:14px;top:26px;height:2px;background:var(--pink)}

/* hero */
.hero{position:absolute;left:0;top:111px;width:1200px;height:542px;background:
  radial-gradient(circle at 78% 30%,rgba(190,80,40,.55),transparent 45%),
  radial-gradient(circle at 25% 40%,rgba(120,120,120,.6),transparent 40%),
  linear-gradient(100deg,#2a2a2a 0%,#1a1512 45%,#3a2418 75%,#120d0a 100%)}
.hero-title{position:absolute;right:103px;top:218px;text-align:right;color:#fff;font-family:"Lato",sans-serif;font-weight:700;font-size:35px;line-height:46px}

/* difference */
.diff-photo{position:absolute;left:99px;top:705px;width:428px;height:303px;border-left:5px solid var(--gold);background:linear-gradient(135deg,#3b2a1d,#7a4a2c 50%,#1e1a18)}
.diff-text{position:absolute;left:552px;top:697px;width:550px}
.diff-text h2{font-size:30px;color:var(--gold);line-height:34px}
.diff-text h3{font-size:20px;color:#333;line-height:24px}
.diff-text .rule{width:150px;height:1px;background:#bbb;margin:18px 0 22px}
.diff-text p{font-size:13px;line-height:22px;color:#333;margin-bottom:14px}

/* what we do */
.what{position:absolute;left:0;top:1060px;width:1200px;height:941px;background:
  radial-gradient(ellipse at 50% 70%,rgba(90,90,100,.55),transparent 55%),
  linear-gradient(#1a1a1c,#0d0d0f)}
.section-title{position:absolute;width:1200px;text-align:center;font-family:"Lato",sans-serif;font-size:30px;letter-spacing:.5px}
.section-rule{position:absolute;left:560px;width:80px;height:2px}
.player{position:absolute;left:172px;top:130px;width:855px;height:444px;border:3px solid #555;background:#111}
.player-bar{height:34px;background:#2b6aa3;color:#fff;font-size:16px;text-align:center;line-height:34px}
.player-screen{position:absolute;left:0;top:34px;width:849px;height:370px;background:linear-gradient(#141414,#0a0a0a)}
.reel-name{position:absolute;left:0;width:849px;text-align:center;top:70px;color:#fff;font-family:"Lato",sans-serif;font-weight:900;font-size:44px}
.reel-year{position:absolute;left:0;width:849px;text-align:center;top:170px;color:#eee;font-family:"Lato",sans-serif;font-weight:300;font-size:68px}
.player-side{position:absolute;right:8px;top:10px;display:flex;flex-direction:column;gap:8px}
.player-side span{width:30px;height:30px;background:#333;border-radius:2px}
.player-controls{position:absolute;left:0;bottom:0;width:849px;height:34px;background:#1f1f1f;display:flex;align-items:center;padding:0 10px;gap:10px}
.player-controls .play{width:40px;height:22px;background:#333;display:flex;align-items:center;justify-content:center}
.player-controls .track{flex:1;height:8px;background:#555}
.player-controls .lbl{color:#aaa;font-size:11px;font-weight:700}
.what-divider{position:absolute;left:99px;top:630px;width:1002px;height:1px;background:#555}
.service{position:absolute;top:676px;width:230px;color:#ddd}
.service-head{display:flex;gap:10px;align-items:flex-start;height:54px}
.service-head h4{font-family:"Lato",sans-serif;font-weight:700;font-size:18px;line-height:22px;color:#fff;text-transform:uppercase}
.service-head h4 em{font-style:normal;color:var(--gold);display:block}
.service ul{list-style:none;margin-top:20px}
.service li{font-size:14px;line-height:34px;display:flex;align-items:center;gap:12px;color:#ccc}
.service li::before{content:"";width:14px;height:11px;border-top:3px solid #888;border-bottom:3px solid #888;background:linear-gradient(#888,#888) center/100% 2px no-repeat}

/* projects */
.tabs{position:absolute;left:466px;top:2131px;display:flex;font-size:14px}
.tabs span{width:133px;height:42px;line-height:40px;text-align:center;border:1px solid var(--gold)}
.tabs .on{background:var(--gold);color:#fff}
.tabs .off{color:var(--gold);background:#fff}
.tile{position:absolute;width:230px;height:190px;border:4px solid var(--blue)}

/* spotlight & testimonial */
.panel{position:absolute;left:0;top:2656px;width:1200px;height:436px;background:var(--grey)}
.panel-title{position:absolute;font-family:"Lato",sans-serif;font-size:30px;color:#333}
.panel-title b{font-weight:400;color:var(--pink)}
.spot{position:absolute;left:99px;width:460px;display:flex;gap:22px}
.spot-thumb{width:116px;height:88px;flex:none}
.spot h5{font-size:14px;font-weight:700;color:#333;margin-bottom:6px}
.spot p{font-size:12px;line-height:18px;color:#666}
.spot time{display:block;font-size:11px;color:#666;margin-top:10px}
.view-all{position:absolute;left:99px;top:3014px;width:90px;height:28px;background:var(--blue);color:#fff;font-size:11px;font-weight:700;text-align:center;line-height:28px}
.panel-divider{position:absolute;left:600px;top:2716px;width:1px;height:330px;background:var(--line)}
.testi-box{position:absolute;left:630px;top:2782px;width:470px;height:230px;background:#d6d6d6;padding:22px 20px}
.testi{display:flex;gap:14px;margin-bottom:22px}
.avatar{width:58px;height:58px;border-radius:50%;background:#9a9a9a;border:3px solid #fff;flex:none}
.testi h6{font-size:13px;font-weight:700;color:#333}
.testi p{font-size:12px;line-height:18px;color:#555}
.testi-nav{position:absolute;left:1045px;top:3014px;display:flex;gap:2px}
.testi-nav span{width:26px;height:20px;background:#c6c6c6}

/* clients */
.client{position:absolute;top:3223px;width:146px;height:76px;border:1px solid #ddd;display:flex;align-items:center;justify-content:center;font-family:"Lato",sans-serif;font-weight:700;font-size:15px;color:#555;text-align:center}

/* footer */
.site-footer{position:absolute;left:0;top:3351px;width:1200px;height:316px;background:var(--footer);color:#ddd}
.foot-col{position:absolute;top:52px}
.foot-col h4{font-family:"Lato",sans-serif;font-weight:700;font-size:17px;color:#fff;margin-bottom:20px;letter-spacing:.5px}
.foot-links{list-style:none;font-size:12.5px;line-height:29px}
.foot-links li::before{content:"› ";color:#aaa}
.field{width:238px;height:26px;background:#3a322f;color:#bbb;font-size:11px;padding:5px 8px;margin-bottom:6px}
.field.big{height:56px}
.submit{width:96px;height:28px;background:var(--pink);color:#fff;font-size:12px;font-weight:700;text-align:center;line-height:28px;margin-top:6px}
.find-row{display:flex;gap:12px;font-size:13px;line-height:19px;margin-bottom:18px;color:#ddd}
.find-ico{width:26px;height:26px;background:var(--pink);flex:none;display:flex;align-items:center;justify-content:center}
.social-list{list-style:none;font-size:13px;line-height:30px}
.social-list li{display:flex;align-items:center;gap:10px}
.social-list li span{width:18px;height:18px;border-radius:50%;background:var(--blue)}
.copyright{position:absolute;left:0;top:3667px;width:1200px;height:29px;background:var(--blue);color:#fff;font-size:12px;font-weight:700;text-align:center;line-height:29px}
</style>
</head>
<body>

<header class="site-header">
  <div class="brand"><span class="brand-mark"></span><span class="brand-name">VELNARO MEDIA</span></div>
  <div class="brand-sub">&amp; ENTERTAINMENT</div>
  <div class="socials-top"><span></span><span></span><span></span><span></span><span></span></div>
  <div class="phone-pill">
    <svg width="14" height="14" viewBox="0 0 24 24"><path fill="#fff" d="M6.6 10.8a15.1 15.1 0 006.6 6.6l2.2-2.2c.3-.3.7-.4 1-.2 1.1.4 2.3.6 3.6.6.6 0 1 .4 1 1V20c0 .6-.4 1-1 1A17 17 0 013 4c0-.6.4-1 1-1h3.5c.6 0 1 .4 1 1 0 1.2.2 2.4.6 3.6.1.3 0 .7-.2 1z"/></svg>
    +1 555 014 2290
  </div>
  <nav class="main-nav">
    <a class="active">HOME</a><a>ABOUT US</a><a>PROJECTS</a><a>CLIENT SPOTLIGHT</a><a>TESTIMONIALS</a><a>CONTACT US</a>
  </nav>
</header>

<section class="hero" role="img" aria-label="Film camera operator recording a live event in warm stage light">
  <h1 class="hero-title">We Specialized In Stylized<br>Commercials, Film Pieces<br>And Live Events.</h1>
</section>

<section>
  <div class="diff-photo" role="img" aria-label="Film crew shooting a scene at a bar"></div>
  <div class="diff-text">
    <h2>THE VELNARO DIFFERENCE</h2>
    <h3>WHO WE ARE</h3>
    <div class="rule"></div>
    <p>Velnaro Media &amp; Entertainment provides full-service campaigns in film and media production, live entertainment &amp; theatrical production, marketing &amp; advertising, and event management in the DC metro area. Founded in 2009, Velnaro Media &amp; Entertainment has built a reputation working for clients including the Harborline Film Guild, Northgate Forum, Calder Music, Riverbend Community Aid, and Brightwell Events.</p>
    <p>Velnaro Media &amp; Entertainment works to build strong relationships with its clients through full-service campaigns in multiple industries. Through community outreach, Velnaro develops its campaigns thoroughly to provide the most successful services to its clients.</p>
  </div>
</section>

<section class="what" role="img" aria-label="Concert crowd with raised hands in front of a stage">
  <h2 class="section-title" style="top:42px;color:#fff">WHAT WE DO</h2>
  <div class="section-rule" style="top:96px;background:#777"></div>

  <div class="player">
    <div class="player-bar">Check Out Our Existing Videos On Streamly</div>
    <div class="player-screen">
      <div class="reel-name">VELNARO MEDIA &amp; ENTERTAINMENT</div>
      <div class="reel-year">2015 Demo Reel</div>
      <div class="player-side"><span></span><span></span><span></span><span></span></div>
    </div>
    <div class="player-controls">
      <div class="play"><svg width="12" height="12" viewBox="0 0 10 10"><path d="M2 1l7 4-7 4z" fill="#fff"/></svg></div>
      <div class="track"></div>
      <span class="lbl">HD</span><span class="lbl">⛶</span><span class="lbl">streamly</span>
    </div>
  </div>

  <div class="what-divider"></div>

  <div class="service" style="left:99px">
    <div class="service-head">
      <svg width="32" height="32" viewBox="0 0 32 32"><circle cx="16" cy="16" r="14" fill="var(--gold)"/><g fill="#141414"><circle cx="16" cy="8" r="3"/><circle cx="16" cy="24" r="3"/><circle cx="8" cy="16" r="3"/><circle cx="24" cy="16" r="3"/></g></svg>
      <h4>Film &amp; Media<em>Production</em></h4>
    </div>
    <ul><li>Design Creative Suite</li><li>Motion Graphics</li><li>4k Workflow</li><li>Direct To Web/Tubeline</li></ul>
  </div>
  <div class="service" style="left:352px">
    <div class="service-head">
      <svg width="32" height="32" viewBox="0 0 32 32"><rect x="4" y="12" width="18" height="12" fill="var(--gold)"/><path d="M22 15l8-4v14l-8-4z" fill="var(--gold)"/><rect x="8" y="24" width="3" height="7" fill="var(--gold)"/><rect x="15" y="24" width="3" height="7" fill="var(--gold)"/></svg>
      <h4>Live<em>Production</em></h4>
    </div>
    <ul><li>Theatrical Producing</li><li>Production Management</li><li>Lighting &amp; Video Design</li><li>Audio System Design</li></ul>
  </div>
  <div class="service" style="left:602px">
    <div class="service-head">
      <svg width="32" height="32" viewBox="0 0 32 32"><rect x="11" y="3" width="10" height="17" rx="5" fill="var(--gold)"/><path d="M7 15a9 9 0 0018 0" stroke="var(--gold)" stroke-width="2.5" fill="none"/><rect x="15" y="24" width="2.5" height="6" fill="var(--gold)"/></svg>
      <h4>PR, Marketing<em>&amp; Advertising</em></h4>
    </div>
    <ul><li>Branding</li><li>Social Media</li><li>Media Relations &amp; Outreach</li><li>Street Teams</li></ul>
  </div>
  <div class="service" style="left:885px">
    <div class="service-head">
      <svg width="32" height="32" viewBox="0 0 32 32"><rect x="4" y="7" width="24" height="21" fill="none" stroke="var(--gold)" stroke-width="2.5"/><rect x="4" y="7" width="24" height="6" fill="var(--gold)"/><g fill="var(--gold)"><rect x="9" y="17" width="4" height="3"/><rect x="15" y="17" width="4" height="3"/><rect x="21" y="17" width="4" height="3"/><rect x="9" y="22" width="4" height="3"/></g></svg>
      <h4 style="padding-top:6px">Events</h4>
    </div>
    <ul><li>Event Production</li><li>Staffing &amp; Hiring</li><li>Manage Rfps</li><li>Sponsor Relations</li></ul>
  </div>
</section>

<section>
  <h2 class="section-title" style="top:2046px;color:#333"><span style="color:var(--blue)">OUR</span> PROJECTS</h2>
  <div class="section-rule" style="top:2100px;background:#ccc"></div>
  <div class="tabs"><span class="on">SHOW ALL</span><span class="off">VIDEO</span></div>

  <div class="tile" style="left:99px;top:2200px;background:linear-gradient(135deg,#f3f0ea,#c94a3a 70%,#e9dcc8)" role="img" aria-label="Show poster with cocktail glass"></div>
  <div class="tile" style="left:357px;top:2200px;background:linear-gradient(#7fb2dc,#8a6a4a 60%,#4a5a3a)" role="img" aria-label="Music school building exterior"></div>
  <div class="tile" style="left:614px;top:2200px;background:linear-gradient(#f2f2f2,#c9a58a 55%,#8a2a30)" role="img" aria-label="Portrait of a speaker in a sports jersey"></div>
  <div class="tile" style="left:867px;top:2200px;background:linear-gradient(120deg,#2a2a2a,#6a6a6a 60%,#111)" role="img" aria-label="Guitar event poster"></div>
  <div class="tile" style="left:99px;top:2415px;background:linear-gradient(#8ab56a,#6a4a3a 60%,#9a9aa8)" role="img" aria-label="Athlete interview outdoors"></div>
  <div class="tile" style="left:357px;top:2415px;background:linear-gradient(#1a2a4a,#3a4a6a 60%,#1a1a2a)" role="img" aria-label="Events at the center poster"></div>
  <div class="tile" style="left:614px;top:2415px;background:linear-gradient(#d8cbb5,#7a6a5a 60%,#3a3a3a)" role="img" aria-label="Two guests at a reception"></div>
  <div class="tile" style="left:867px;top:2415px;background:linear-gradient(#5a4a3a,#8a7a6a 50%,#2a2a2a)" role="img" aria-label="Business speaker in an office"></div>
</section>

<section class="panel"></section>
<h2 class="panel-title" style="left:99px;top:2700px"><b>CLIENT</b> SPOTLIGHT</h2>
<div class="spot" style="top:2782px">
  <div class="spot-thumb" role="img" aria-label="Concert crowd under stage lights" style="background:linear-gradient(#3a2a1a,#b86a2a 55%,#1a1a1a)"></div>
  <div><h5>Lorem ipsum dolor sit&nbsp; consectetuer adipis.</h5><p>Sed diam nonummy nibh euismod tincidunt ut laoreet dolore magna aliquam erat volutpat...[+]</p><time>📅 January 6, 2017</time></div>
</div>
<div class="spot" style="top:2900px">
  <div class="spot-thumb" role="img" aria-label="Festival crowd at sunset" style="background:linear-gradient(#f0c070,#c86a2a 55%,#2a1a1a)"></div>
  <div><h5>Lorem ipsum dolor sit&nbsp; consectetuer adipis.</h5><p>Sed diam nonummy nibh euismod tincidunt ut laoreet dolore magna aliquam erat volutpat...[+]</p><time>📅 January 6, 2017</time></div>
</div>
<div class="view-all">VIEW ALL</div>
<div class="panel-divider"></div>
<h2 class="panel-title" style="left:630px;top:2700px"><b>CLIENT</b> TESTIMONIAL</h2>
<div class="testi-box">
  <div class="testi"><div class="avatar" role="img" aria-label="Client portrait"></div><div><h6>Mr. Daniel Pereth</h6><p>Lorem ipsum dolor sit amet, consectetuer adipiscing elit, sed diam nonummy nibh euismod tincidunt ut laoreet dolore magna aliquam erat volutpat. Ut wisi enim ad minim veniam.</p></div></div>
  <div class="testi"><div class="avatar" role="img" aria-label="Client portrait"></div><div><h6>Miss. Laura Pereth</h6><p>Lorem ipsum dolor sit amet, consectetuer adipiscing elit, sed diam nonummy nibh euismod tincidunt ut laoreet dolore magna aliquam erat volutpat. Ut wisi enim ad minim veniam.</p></div></div>
</div>
<div class="testi-nav"><span></span><span></span></div>

<section>
  <h2 class="section-title" style="top:3134px;color:#333">OUR CLIENTS</h2>
  <div class="section-rule" style="top:3186px;background:#ccc"></div>
  <svg class="abs" style="left:52px;top:3240px" width="20" height="44" viewBox="0 0 20 44"><path d="M18 2L3 22l15 20" stroke="#bbb" stroke-width="2" fill="none"/></svg>
  <svg class="abs" style="left:1122px;top:3240px" width="20" height="44" viewBox="0 0 20 44"><path d="M2 2l15 20L2 42" stroke="#bbb" stroke-width="2" fill="none"/></svg>
  <div class="client" style="left:99px">Harborline Docs</div>
  <div class="client" style="left:268px">Calder Music</div>
  <div class="client" style="left:442px">Riverbend</div>
  <div class="client" style="left:613px">Gearlet</div>
  <div class="client" style="left:783px">Northgate</div>
  <div class="client" style="left:952px">Quorvex</div>
</section>

<footer class="site-footer">
  <div class="foot-col" style="left:99px">
    <h4>QUICK LINK</h4>
    <ul class="foot-links"><li>Home</li><li>About Us</li><li>Projects</li><li>Client Spotlight</li><li>Testimonial</li><li>Contact Us</li></ul>
  </div>
  <div class="foot-col" style="left:283px">
    <h4>QUICK CONTACT</h4>
    <div class="field">Name</div><div class="field">Email</div><div class="field big">Message</div>
    <div class="submit">SUBMIT</div>
  </div>
  <div class="foot-col" style="left:596px">
    <h4>FIND US</h4>
    <div class="find-row"><span class="find-ico"><svg width="12" height="14" viewBox="0 0 12 16"><path d="M6 0a6 6 0 00-6 6c0 4.5 6 10 6 10s6-5.5 6-10a6 6 0 00-6-6zm0 8.5A2.5 2.5 0 116 3.5a2.5 2.5 0 010 5z" fill="#fff"/></svg></span><div>Velnaro Media &amp; Entertainment<br>4417 Larchmere Lane #210<br>Westbrook, MD 20990</div></div>
    <div class="find-row"><span class="find-ico"><svg width="13" height="13" viewBox="0 0 24 24"><path fill="#fff" d="M6.6 10.8a15.1 15.1 0 006.6 6.6l2.2-2.2c.3-.3.7-.4 1-.2 1.1.4 2.3.6 3.6.6.6 0 1 .4 1 1V20c0 .6-.4 1-1 1A17 17 0 013 4c0-.6.4-1 1-1h3.5c.6 0 1 .4 1 1 0 1.2.2 2.4.6 3.6.1.3 0 .7-.2 1z"/></svg></span><div style="line-height:26px">+1 555 014 2290</div></div>
    <div class="find-row"><span class="find-ico"><svg width="14" height="11" viewBox="0 0 16 12"><rect x="0" y="0" width="16" height="12" fill="#fff"/><path d="M0 0l8 7 8-7" stroke="var(--pink)" stroke-width="1.5" fill="none"/></svg></span><div style="line-height:26px">info@zantorvo.com</div></div>
  </div>
  <div class="foot-col" style="left:920px">
    <h4>SOCIAL MEDIA</h4>
    <ul class="social-list"><li><span></span>Friendcast</li><li><span></span>Chirplet</li><li><span></span>Workweave</li><li><span></span>Tubeline</li><li><span></span>Streamly</li></ul>
  </div>
</footer>
<div class="copyright">Copyright © 2016 Velnaro Media &amp; Entertainment. All Rights Reserved.</div>

</body>
</html>
```